PulseLedgerPro.Com PowerPoint

I need a PowerPoint layout for my presentations. My business is called PulseLedgerPro.Com - my presentations teach cardiologists how to document their procedures and visits and teaches them how to bill accurately for them.

Industry/Entity Type

Business

Requirements
Must have
• the logo should be subtly there on each page - perhaps as a watermark? I'm really not creative; please help.

```html
<!DOCTYPE html>
<html lang="en">
<head>
<meta charset="utf-8">
<title>PulseLedgerPro.Com Presentation Layout</title>
<link rel="stylesheet" href="https://fonts.googleapis.com/css2?family=PT+Sans+Narrow:wght@700&family=Carlito:wght@400;700&display=swap">
<style>
  :root {
    --page: #ffffff;
    --slide-light: #f7f7f5;
    --slide-mid: #e4e4e2;
    --olive: #9c8a22;
    --olive-dark: #8a7a1c;
    --gold-deep: #b99a3c;
    --gold-light: #e9e58c;
    --pale-ring: #eeeeb4;
    --pale-fill: #dfe08a;
    --heart-red: #d9261a;
    --brand-red: #c0281f;
    --ink: #1c1c1c;
    --row-a: #e4e6b6;
    --row-b: #f0f1d9;
    --shadow: rgba(0,0,0,0.28);
  }
  * { box-sizing: border-box; margin: 0; padding: 0; }
  html, body { width: 1200px; height: 735px; overflow: hidden; background: var(--page); }
  body { position: relative; font-family: "Carlito", "Calibri", sans-serif; color: var(--ink); }

  .slide {
    position: absolute;
    overflow: hidden;
    background: radial-gradient(ellipse at 45% 35%, var(--slide-light) 0%, var(--slide-mid) 100%);
    box-shadow: 4px 5px 8px var(--shadow);
  }
  .slide-art { position: absolute; inset: 0; width: 100%; height: 100%; }

  /* Title slide */
  .slide--title { left: 35px; top: 60px; width: 727px; height: 547px; }
  .title-heading {
    position: absolute; left: 31px; top: 232px;
    font-family: "PT Sans Narrow", "Arial Narrow", sans-serif;
    font-weight: 700; font-size: 45px; line-height: 48px;
    color: var(--olive); text-transform: uppercase; letter-spacing: 0.5px;
  }
  .brand {
    position: absolute; display: flex; align-items: center; gap: 6px;
    font-family: "Carlito", "Calibri", sans-serif; font-weight: 700; color: var(--brand-red);
  }
  .brand-dot { border-radius: 50%; background: var(--brand-red); flex: none; }
  .brand--large { left: 31px; top: 392px; font-size: 24px; }
  .brand--large .brand-dot { width: 26px; height: 26px; }
  .site-address {
    position: absolute; right: 42px; bottom: 12px;
    font-weight: 700; font-size: 15px; color: #111;
  }

  /* Content slides */
  .slide--content { left: 778px; width: 393px; height: 294px; }
  .slide--text { top: 60px; }
  .slide--table { top: 372px; }
  .brand--small { right: 12px; top: 10px; font-size: 10px; gap: 3px; }
  .brand--small .brand-dot { width: 10px; height: 10px; }
  .section-heading {
    font-weight: 700; font-size: 9.5px; color: var(--olive);
    margin-bottom: 14px;
  }
  .slide-body { position: absolute; left: 21px; right: 20px; top: 42px; }
  .body-copy { font-size: 7.6px; line-height: 10.6px; text-align: justify; margin-bottom: 18px; }
  .body-copy strong { font-weight: 700; }

  .data-table {
    position: absolute; left: 22px; top: 147px; width: 196px;
    border-collapse: collapse; font-size: 7.6px; text-align: center;
  }
  .data-table th {
    background: var(--olive); color: #fff; font-weight: 700;
    height: 19px; border-right: 1px solid #fff;
  }
  .data-table td { height: 16.5px; color: #555; border-right: 1px solid #fff; border-top: 1px solid #fff; }
  .data-table tr:nth-child(odd) td { background: var(--row-a); }
  .data-table tr:nth-child(even) td { background: var(--row-b); }
  .data-table th:last-child, .data-table td:last-child { border-right: none; }

  .service-list {
    position: absolute; left: 223px; top: 145px; width: 155px;
    list-style: none; font-size: 7.6px; line-height: 10.4px;
  }
  .service-list li::before { content: "\2022 "; color: var(--brand-red); }
</style>
</head>
<body>

<section class="slide slide--title">
  <svg class="slide-art" viewBox="0 0 757 570" preserveAspectRatio="none">
    <defs>
      <linearGradient id="goldBand" x1="0" y1="0" x2="1" y2="0">
        <stop offset="0" stop-color="#c9ad55"/>
        <stop offset="0.35" stop-color="#e6df8a"/>
        <stop offset="0.65" stop-color="#ece68e"/>
        <stop offset="1" stop-color="#b99a3c"/>
      </linearGradient>
    </defs>
    <g class="bg-lines" fill="none" stroke="#ffffff" stroke-width="1.2" opacity="0.9">
      <path d="M0,330 C150,250 300,520 757,360"/>
      <path d="M0,360 C170,280 320,500 757,390"/>
      <path d="M0,300 C200,420 420,300 757,430"/>
      <path d="M80,570 C150,350 260,250 330,0"/>
      <path d="M600,0 C640,200 700,300 757,320"/>
      <path d="M520,0 C600,250 690,260 757,270"/>
    </g>
    <path class="gold-band" d="M0,485 C160,515 300,455 470,440 C600,428 690,430 757,432 L757,570 L0,570 Z" fill="url(#goldBand)"/>
    <path class="gold-shine" d="M0,500 C200,540 380,470 757,470 L757,480 C400,482 220,548 0,515 Z" fill="#f5f2b8" opacity="0.8"/>
    <path d="M0,530 C220,560 420,500 757,500" fill="none" stroke="#f5f0a0" stroke-width="1.5"/>

    <g class="callouts" stroke="var(--pale-ring)" stroke-width="5" fill="none">
      <path d="M361,92 L361,168 L452,168"/>
      <path d="M610,177 L548,177"/>
      <path d="M407,242 L497,242"/>
    </g>
    <g class="callout-dots">
      <circle cx="361" cy="45" r="48" fill="var(--pale-ring)"/>
      <circle cx="361" cy="45" r="41" fill="var(--pale-fill)"/>
      <circle cx="644" cy="157" r="36" fill="var(--pale-ring)"/>
      <circle cx="644" cy="157" r="30" fill="var(--pale-fill)"/>
      <circle cx="381" cy="243" r="28" fill="var(--pale-ring)"/>
      <circle cx="381" cy="243" r="22" fill="var(--pale-fill)"/>
    </g>
    <rect x="432" y="40" width="140" height="230" rx="55" fill="var(--heart-red)" role="img" aria-label="Illustration of a red human heart"/>
  </svg>
  <h1 class="title-heading">Title<br>of the<br>presentation</h1>
  <div class="brand brand--large"><span class="brand-dot"></span>PulseLedgerPro.Com</div>
  <p class="site-address">pulseledgerpro.com</p>
</section>

<section class="slide slide--content slide--text">
  <svg class="slide-art" viewBox="0 0 409 306" preserveAspectRatio="none">
    <g fill="none" stroke="#ffffff" stroke-width="1" opacity="0.9">
      <path d="M0,250 C120,200 250,320 409,240"/>
      <path d="M200,306 C260,200 340,150 409,140"/>
    </g>
    <path d="M0,296 C140,300 280,285 409,280 L409,306 L0,306 Z" fill="var(--gold-deep)"/>
    <path d="M0,298 C150,292 300,290 409,288 L409,292 C300,294 150,297 0,302 Z" fill="var(--gold-light)"/>
  </svg>
  <div class="brand brand--small"><span class="brand-dot"></span>PulseLedgerPro.Com</div>
  <div class="slide-body">
    <h2 class="section-heading">Lorem Ipsum</h2>
    <p class="body-copy"><strong>Lorem Ipsum</strong> is simply dummy text of the printing and typesetting industry. Lorem Ipsum has been the industry's standard dummy text ever since the 1500s, when an unknown printer took a galley of type and scrambled it to make a type specimen book. It has survived not only five centuries, but also the leap into electronic typesetting, remaining essentially unchanged. It was popularised in the 1960s with the release of Typeline sheets containing Lorem Ipsum passages, and more recently with desktop publishing software like Quillset Composer including versions of Lorem Ipsum.</p>
    <h2 class="section-heading">Lorem Ipsum</h2>
    <p class="body-copy"><strong>Lorem Ipsum</strong> is simply dummy text of the printing and typesetting industry. Lorem Ipsum has been the industry's standard dummy text ever since the 1500s, when an unknown printer took a galley of type and scrambled it to make a type specimen book. It has survived not only five centuries, but also the leap into electronic typesetting, remaining essentially unchanged. It was popularised in the 1960s with the release of Typeline sheets containing Lorem Ipsum passages, and more recently with desktop publishing software like Quillset Composer including versions of Lorem Ipsum.</p>
  </div>
</section>

<section class="slide slide--content slide--table">
  <svg class="slide-art" viewBox="0 0 409 306" preserveAspectRatio="none">
    <g fill="none" stroke="#ffffff" stroke-width="1" opacity="0.9">
      <path d="M0,250 C120,200 250,320 409,240"/>
      <path d="M200,306 C260,200 340,150 409,140"/>
    </g>
    <path d="M0,296 C140,300 280,285 409,280 L409,306 L0,306 Z" fill="var(--gold-deep)"/>
    <path d="M0,298 C150,292 300,290 409,288 L409,292 C300,294 150,297 0,302 Z" fill="var(--gold-light)"/>
  </svg>
  <div class="brand brand--small"><span class="brand-dot"></span>PulseLedgerPro.Com</div>
  <div class="slide-body">
    <h2 class="section-heading">Lorem Ipsum</h2>
    <p class="body-copy"><strong>Lorem Ipsum</strong> is simply dummy text of the printing and typesetting industry. Lorem Ipsum has been the industry's standard dummy text ever since the 1500s, when an unknown printer took a galley of type and scrambled it to make a type specimen book. It has survived not only five centuries, but also the leap into electronic typesetting, remaining essentially unchanged. It was popularised in the 1960s with the release of Typeline sheets containing Lorem Ipsum passages, and more recently with desktop publishing software like Quillset Composer including versions of Lorem Ipsum.</p>
  </div>
  <table class="data-table">
    <thead>
      <tr><th>Least Sheets</th><th>Lorem</th><th>Lorem</th><th>Lorem</th></tr>
    </thead>
    <tbody>
      <tr><td>Least Sheets</td><td>Lorem</td><td>Lorem</td><td>Lorem</td></tr>
      <tr><td>Least Sheets</td><td>Lorem</td><td>Lorem</td><td>Lorem</td></tr>
      <tr><td>Least Sheets</td><td>Lorem</td><td>Lorem</td><td>Lorem</td></tr>
      <tr><td>Least Sheets</td><td>Lorem</td><td>Lorem</td><td>Lorem</td></tr>
    </tbody>
  </table>
  <ul class="service-list">
    <li>We execute proprietary checks and balances to make sure that we bill each reportable service.</li>
    <li>Dana Reyes, CPC, CCC provides physician training to ensure that documentation is adequate.</li>
    <li>We conduct chart audits to screen for regulatory exposure and improvement opportunities.</li>
    <li>Our staff of over one hundred employees works exclusively from our United States based offices.</li>
  </ul>
</section>

</body>
</html>
```